Re-Design of existing Shopify Website

Hi,

We are looking for a skilled person to work with us on improving the design of our website to make it more user friendly. We are a Makeup brush and makeup accessories company and our current website can be viewed at pillowandfern dot com.We are looking to simplify the layout and make it more modern and mobile friendly.

We have designs in mind which we would like to implement to our site which we feel would work better for us to increase traffic and sales.

We would like the layout to have clear sections for brushes,lashes ,sponge and also our tutorials on the landing page.

Industry/Entity Type

Hair And Beauty

Number of Pages Required

5+ page

Font styles to use
Sans Serif

Colors
b8a6cd
d3a5cc
eea4c8
ffffff
000000

Requirements
Must have
• -Clear ,modern landing page.
• -easy navigation
• -simple design
• -professional design approach
Nice to have
• cross selling pop up
Should not have
• over use of bold colour.

```html
<!DOCTYPE html>
<html lang="en">
<head>
<meta charset="utf-8">
<title>Pillow &amp; Fern — Makeup Brushes &amp; Accessories</title>
<link href="https://fonts.googleapis.com/css2?family=Montserrat:wght@400;500;600;700&family=Open+Sans:wght@400;600&display=swap" rel="stylesheet">
<style>
  :root{
    --pink:#f08fb5;
    --pink-soft:#f6bfd3;
    --pink-pale:#f9d3e1;
    --pink-band:#f3a5c5;
    --maroon:#4d1b1f;
    --ink:#2a2a2a;
    --grey-text:#555;
    --light-bg:#f2f2f2;
    --footer-bg:#d7d7d7;
    --accent:#f0612e;
    --gold:#f2a51c;
    --white:#ffffff;
  }
  *{box-sizing:border-box;margin:0;padding:0}
  html,body{width:1200px;height:3354px;overflow:hidden}
  body{position:relative;background:var(--white);font-family:'Open Sans',sans-serif;color:var(--ink)}
  .abs{position:absolute}

  /* Hero */
  .hero{left:0;top:0;width:1200px;height:624px;background:linear-gradient(100deg,#5a3a2c 0%,#b88a6c 35%,#a27a60 60%,#7a5a48 100%)}
  .brand{left:34px;top:40px;font-family:'Montserrat',sans-serif;font-weight:600;font-size:40px;line-height:1.05;color:var(--pink)}
  .nav{left:475px;top:38px;display:flex;gap:38px;font-family:'Montserrat',sans-serif;font-size:11px;font-weight:500;letter-spacing:.5px;color:var(--white)}
  .nav-icons{left:955px;top:32px;display:flex;gap:22px}
  .hero-copy{left:660px;top:134px;font-family:'Montserrat',sans-serif;color:var(--white)}
  .hero-copy .lead{font-size:30px;font-weight:400;margin-bottom:8px}
  .hero-copy .line{font-size:36px;font-weight:700;letter-spacing:1.5px;line-height:48px}
  .hero-copy .dark{color:var(--maroon)}
  .slider-dots{left:1006px;top:468px;display:flex;gap:6px}
  .slider-dots span{width:11px;height:11px;border:1px solid #e8d3c6}
  .slider-dots .on{background:var(--gold);border-color:var(--gold)}

  /* Category tiles */
  .tile{top:624px;width:400px;height:227px;display:flex;flex-direction:column;align-items:center;justify-content:center;font-family:'Montserrat',sans-serif;text-align:center}
  .tile-brushes{left:0;background:linear-gradient(90deg,#e9e6e4,#f6f3f1)}
  .tile-lashes{left:400px;background:#1d1b1b;border:9px solid #6a6a6a;color:var(--white)}
  .tile-sponge{left:800px;background:linear-gradient(90deg,#f1e4e0,#f7e9e6)}
  .tile .kicker{font-size:14px;font-weight:500;letter-spacing:.5px}
  .tile .name{font-size:40px;font-weight:700;letter-spacing:1px;line-height:44px}
  .tile-brushes .name,.tile-sponge .name{color:var(--maroon)}
  .tile .small{font-size:10px;color:var(--white);letter-spacing:1px}
  .tile .btn-outline{margin-top:8px;border:1.5px solid var(--accent);color:var(--accent);font-size:9px;padding:5px 14px;letter-spacing:1px}

  /* About */
  .about-photo{left:206px;top:890px;width:329px;height:491px;background:linear-gradient(160deg,#3a3334,#7b6b6a 55%,#2b2526)}
  .about-copy{left:610px;top:1020px;width:430px}
  .section-title{font-family:'Montserrat',sans-serif;font-weight:600;font-size:30px;color:var(--pink);line-height:38px}
  .about-copy p{margin-top:22px;font-size:14px;line-height:23px;color:var(--grey-text)}
  .btn-pill{display:inline-block;margin-top:28px;width:202px;height:46px;line-height:46px;border-radius:23px;background:var(--pink);color:var(--white);text-align:center;font-family:'Montserrat',sans-serif;font-weight:700;font-size:13px;letter-spacing:.5px}

  /* Beauty band */
  .beauty-band{left:0;top:1422px;width:1200px;height:471px;background:linear-gradient(180deg,#f1a3c2 0%,#f4a9c7 50%,#f2a0c1 100%)}
  .beauty-copy{left:300px;top:1598px;width:600px;text-align:center;font-family:'Montserrat',sans-serif}
  .beauty-copy h2{font-size:30px;line-height:40px;letter-spacing:2px;color:var(--ink);font-weight:400}
  .beauty-copy h2 b{font-weight:700}
  .beauty-copy p{margin:20px auto 0;width:470px;font-family:'Open Sans',sans-serif;font-size:11.5px;line-height:19px;color:#6b4555}
  .btn-frame{left:539px;top:1796px;width:165px;height:42px;border:1.5px solid var(--accent);color:var(--white);font-family:'Montserrat',sans-serif;font-size:11px;font-weight:600;letter-spacing:1px;display:flex;align-items:center;justify-content:center}

  /* Tutorials */
  .tutorials{left:0;top:1893px;width:1200px;height:734px;background:var(--light-bg)}
  .tutorials-head{left:0;top:1958px;width:1200px;text-align:center}
  .tutorials-head p{margin:14px auto 0;width:470px;font-size:14px;line-height:23px;color:var(--grey-text)}
  .video{left:303px;top:2108px;width:592px;height:360px;border-radius:4px;background:linear-gradient(90deg,#a89a96,#d9cbc6 50%,#a8998f);box-shadow:0 18px 40px rgba(0,0,0,.22)}
  .play{left:539px;top:2233px}
  .video-arrows{left:572px;top:2514px;display:flex;gap:16px}

  /* Instagram strip */
  .insta-photo{top:2627px;width:172px;height:183px}
  .insta-bar{left:0;top:2810px;width:1200px;height:53px;background:var(--pink);border:1.5px solid #f4a060;display:flex;align-items:center;justify-content:center;gap:8px;color:var(--white);font-family:'Montserrat',sans-serif;font-size:15px}
  .insta-bar .square{width:14px;height:14px;border:2px solid var(--white);border-radius:3px}

  /* Newsletter */
  .newsletter{left:0;top:2863px;width:1200px;height:165px;background:var(--pink-soft)}
  .newsletter h3{position:absolute;left:145px;top:52px;font-family:'Montserrat',sans-serif;font-weight:700;font-size:17px;letter-spacing:.8px;color:var(--white)}
  .newsletter p{position:absolute;left:145px;top:80px;width:380px;font-size:11px;line-height:16px;color:#fbe0ea}
  .newsletter .field{position:absolute;left:707px;top:57px;width:351px;height:46px;background:var(--pink-pale);border-radius:2px}
  .newsletter .field svg{position:absolute;right:20px;top:16px}

  /* Footer */
  .footer{left:0;top:3028px;width:1200px;height:223px;background:var(--footer-bg)}
  .footer-brand{left:0;top:3090px;width:1200px;text-align:center;font-family:'Montserrat',sans-serif;font-weight:600;font-size:38px;color:var(--pink)}
  .footer-links{left:0;top:3226px;width:1200px;display:flex;justify-content:center;gap:22px;font-family:'Montserrat',sans-serif;font-size:10px;letter-spacing:.5px;color:#555}
  .social{left:0;top:3251px;width:1200px;height:52px;background:var(--white);border-bottom:1px solid #e0e0e0;display:flex;justify-content:center;align-items:center;gap:16px}
  .social span{width:12px;height:12px;border-radius:50%;background:var(--gold)}
  .copyright{left:0;top:3303px;width:1200px;height:51px;display:flex;align-items:center;justify-content:center;font-family:'Montserrat',sans-serif;font-size:9px;color:#444;letter-spacing:.3px}
</style>
</head>
<body>

<!-- Hero -->
<div class="abs hero" role="img" aria-label="Close-up of a woman in profile applying red lipstick with a lip brush"></div>
<div class="abs brand">Pillow<br>&amp; Fern</div>
<nav class="abs nav">
  <span>SERVICES</span><span>ABOUT US</span><span>CONTACT US</span><span>MY BOOKING</span><span>SALE!</span>
</nav>
<div class="abs nav-icons">
  <svg width="20" height="20" viewBox="0 0 20 20" fill="none" stroke="#fff" stroke-width="1.5"><path d="M1 3h3l2 10h10l2-7H5"/><circle cx="8" cy="17" r="1.3"/><circle cx="15" cy="17" r="1.3"/><circle cx="16" cy="3" r="3" fill="#f2a51c" stroke="none"/></svg>
  <svg width="18" height="18" viewBox="0 0 18 18" fill="none" stroke="#fff" stroke-width="1.6"><circle cx="7.5" cy="7.5" r="5.5"/><path d="M11.5 11.5l5 5"/></svg>
  <svg width="18" height="18" viewBox="0 0 18 18" fill="none" stroke="#fff" stroke-width="1.5"><circle cx="9" cy="6" r="4"/><path d="M2 17c1-4 4-6 7-6s6 2 7 6"/></svg>
</div>
<div class="abs hero-copy">
  <div class="lead">We are</div>
  <div class="line"><span class="dark">MAKEUP BRUSH</span> AND</div>
  <div class="line dark">MAKEUP ACCESSORIES</div>
  <div class="line">COMPANY</div>
</div>
<div class="abs slider-dots"><span class="on"></span><span></span><span></span></div>

<!-- Category tiles -->
<div class="abs tile tile-brushes" role="img" aria-label="Woman holding a fan of makeup brushes">
  <div class="name">BRUSHES</div>
  <div class="small">BIG SALE</div>
</div>
<div class="abs tile tile-lashes" role="img" aria-label="Eye with false lashes being applied">
  <div class="kicker">NEW TREND</div>
  <div class="name">LASHES</div>
  <div class="btn-outline">SHOP NOW</div>
</div>
<div class="abs tile tile-sponge" role="img" aria-label="Woman holding a pink makeup sponge">
  <div class="kicker">NEW TREND</div>
  <div class="name">SPONGE</div>
</div>

<!-- About -->
<div class="abs about-photo" role="img" aria-label="Portrait of a model with purple smoky eye makeup"></div>
<div class="abs about-copy">
  <h2 class="section-title">A Few Words About<br>Our Company</h2>
  <p>Lorem ipsum dolor sit amet, consectetuer adipiscing elit, sed diam nonummy nibh euismod tincidunt ut laoreet dolore magna aliquam erat volutpat wisi enim ad minim veniam, quis nostrud exerci tation ullamcorper suscipit lobortis.</p>
  <span class="btn-pill">SHOW MORE</span>
</div>

<!-- Beauty band -->
<div class="abs beauty-band" role="img" aria-label="Flat lay of brushes, lipstick, compact, blush and glasses on a pink surface"></div>
<div class="abs beauty-copy">
  <h2><b>EVERYTHING HAS</b> BEAUTY<br><b>MAKE UP IS</b> ART</h2>
  <p>Duis autem vel eum iriure dolor in hendrerit in vulputate velit esse molestie consequat, vel illum dolore eu feugiat nulla facilisis at vero eros et accumsan et iusto odio dignissim qui blandit praesent luptatum.</p>
</div>
<div class="abs btn-frame">LEARN MORE</div>

<!-- Tutorials -->
<div class="abs tutorials"></div>
<div class="abs tutorials-head">
  <h2 class="section-title">Watch Our Video Tutorials</h2>
  <p>Investigationes demonstraverunt lectores legere me lius quod ii legunt saepius. Claritas est etiam processus dynamicus.</p>
</div>
<div class="abs video" role="img" aria-label="Video still of a model applying red lipstick"></div>
<svg class="abs play" width="120" height="110" viewBox="0 0 120 110"><circle cx="56" cy="55" r="50" fill="rgba(0,0,0,.25)" stroke="#fff" stroke-width="4"/><path d="M44 33v44l36-22z" fill="#fff"/></svg>
<div class="abs video-arrows">
  <svg width="14" height="24" viewBox="0 0 14 24" fill="none" stroke="#bbb" stroke-width="2.5"><path d="M12 2L3 12l9 10"/></svg>
  <svg width="14" height="24" viewBox="0 0 14 24" fill="none" stroke="#555" stroke-width="2.5"><path d="M2 2l9 10-9 10"/></svg>
</div>

<!-- Instagram strip -->
<div class="abs insta-photo" style="left:0;background:linear-gradient(135deg,#e8dfe0,#c8d6e0)" role="img" aria-label="Pastel eye makeup close-up"></div>
<div class="abs insta-photo" style="left:171px;background:linear-gradient(135deg,#3a2a26,#c89c84)" role="img" aria-label="Model with eyeliner and brush"></div>
<div class="abs insta-photo" style="left:343px;background:linear-gradient(135deg,#e07a4a,#e9c0a8)" role="img" aria-label="Red-haired model holding brushes"></div>
<div class="abs insta-photo" style="left:514px;background:linear-gradient(135deg,#2a2220,#d4a078)" role="img" aria-label="Model with bold lipstick and a blending brush"></div>
<div class="abs insta-photo" style="left:686px;background:linear-gradient(135deg,#5a3a24,#b07a50)" role="img" aria-label="Model applying eye makeup"></div>
<div class="abs insta-photo" style="left:857px;background:linear-gradient(135deg,#f4f0ee,#d8b8a8)" role="img" aria-label="Model applying mascara"></div>
<div class="abs insta-photo" style="left:1029px;background:linear-gradient(135deg,#e6eef2,#c8dbe6)" role="img" aria-label="Soft blue eye makeup close-up"></div>
<div class="abs insta-bar"><span class="square"></span>@pillowandfern</div>

<!-- Newsletter -->
<section class="abs newsletter">
  <h3>SUBSCRIBE OUR NEWSLETTER</h3>
  <p>Get new arrivals, tutorials and members-only offers straight to your inbox every week.</p>
  <div class="field">
    <svg width="20" height="14" viewBox="0 0 20 14" fill="none" stroke="#fff" stroke-width="1.6"><path d="M1 7h17M12 1l6 6-6 6"/></svg>
  </div>
</section>

<!-- Footer -->
<div class="abs footer"></div>
<div class="abs footer-brand">Pillow &amp; Fern</div>
<div class="abs footer-links">
  <span>ABOUT US</span><span>CONTACT US</span><span>BLOG</span><span>OUR SERVICES</span><span>FAQ</span><span>PACKAGES</span>
</div>
<div class="abs social"><span></span><span></span><span></span><span></span></div>
<div class="abs copyright">Copyrights 2016 | ALL RIGHTS RESERVED</div>

</body>
</html>
```